Job advert for Forged by Circle

I would like a poster graphic that I can promote on social media to advertise a job vacancy we will be promoting our upcoming jobs, here is the text...

WE ARE ON THE…

LOOKOUT
(maybe insert graphic or icon that fits with the message here)

For A

OPERATIONS AND HR MANAGER

MEMBERSHIP ADVISOR (EAST MIDLANDS)

SOCIAL MEDIA CONTENT CREATOR

THE UK’s FASTEST GROWING NETWORK FOR MANUFACTURERS

OFFICES IN BIRMINGHAM AND LEEDS - WE ARE AN INCLUSIVE EMPLOYER (use the equality logo provided here)

Target Market(s)

people looking to find a new job

Industry/Entity Type

Manufacture

Font styles to use
Sans Serif

Colors
f04a50
f68e4e
e667a6

Requirements
Must have
• Clear simple and contemporary style
Nice to have
• a nice graphic or icon to convey the text message
Should not have
• use of dark depressing colours

```html
<!DOCTYPE html>
<html lang="en">
<head>
<meta charset="utf-8">
<title>Job Vacancies Poster</title>
<link rel="stylesheet" href="https://fonts.googleapis.com/css2?family=Josefin+Sans:wght@300;400;600;700&display=swap">
<style>
  :root {
    --page-bg: #e6e6e7;
    --paper: #ffffff;
    --brand-red: #ee4650;
    --brand-red-deep: #e33f49;
    --brand-orange: #f39150;
    --brand-orange-light: #f4a066;
    --ink: #4d4d4f;
    --ink-soft: #6a6a6c;
    --on-accent: #ffffff;
  }
  * { margin: 0; padding: 0; box-sizing: border-box; }
  html, body {
    width: 1200px; height: 1178px; overflow: hidden;
    background: var(--page-bg);
    font-family: "Josefin Sans", "Helvetica Neue", Arial, sans-serif;
  }
  .stage { position: relative; width: 1200px; height: 1178px; }
  .poster {
    position: absolute; left: 219px; top: 0;
    width: 740px; height: 1143px;
    background: var(--paper);
    transform: scale(1.0306); transform-origin: top left;
    overflow: hidden;
  }
  .poster__shapes { position: absolute; inset: 0; }
  .tile--red { fill: var(--brand-red); }
  .tile--red-deep { fill: var(--brand-red-deep); }
  .tile--orange { fill: var(--brand-orange-light); }
  .role-band { fill: var(--brand-orange); }

  .mark { position: absolute; left: 332px; top: 50px; display: flex; align-items: center; gap: 14px; }
  .mark__dot { width: 123px; height: 123px; border-radius: 50%; background: var(--brand-red); }
  .mark__name {
    font-weight: 600; font-size: 36px; line-height: 32px; color: var(--ink);
    letter-spacing: -0.5px; padding-top: 8px;
  }

  .headline { position: absolute; right: 50px; top: 228px; text-align: right; color: var(--ink); font-weight: 300; }
  .headline__lead, .headline__tail { font-weight: 300; font-size: 49px; line-height: 52px; letter-spacing: 0.5px; }
  .headline__key { font-weight: 600; font-size: 78px; line-height: 80px; color: var(--brand-red); margin-top: 4px; }

  .roles {
    position: absolute; right: 50px; top: 504px; text-align: right;
    color: var(--on-accent); list-style: none;
  }
  .roles__item { font-weight: 300; font-size: 29px; line-height: 29px; letter-spacing: 1.5px; margin-bottom: 28px; }

  .tagline {
    position: absolute; right: 50px; top: 800px; text-align: right;
    color: var(--ink-soft); font-size: 20px; line-height: 27px; font-weight: 300;
  }
  .tagline strong { font-weight: 700; font-size: 19px; color: var(--ink); }

  .footer {
    position: absolute; right: 50px; top: 1044px; text-align: right;
    color: var(--ink-soft); font-size: 20px; line-height: 27px; font-weight: 300;
  }
  .footer__note { font-weight: 700; font-size: 14px; color: var(--ink); letter-spacing: 0; }
</style>
</head>
<body>
<main class="stage">
  <article class="poster">
    <svg class="poster__shapes" viewBox="0 0 740 1143" width="740" height="1143">
      <g role="img" aria-label="Geometric tiles filled with a warm red and orange photograph of tall city buildings">
        <polygon class="tile--red" points="20,140 167,285 20,430"/>
        <polygon class="tile--red-deep" points="185,305 335,452 185,600 37,452"/>
        <polygon class="tile--orange" points="20,475 167,622 20,765"/>
        <polygon class="tile--red-deep" points="185,642 335,788 185,935 37,788"/>
        <polygon class="tile--red" points="20,810 167,960 20,1100"/>
        <polygon class="tile--red" points="352,807 502,955 352,1103 205,955"/>
        <polygon class="tile--orange" points="37,1122 185,975 335,1122"/>
      </g>
      <polygon class="role-band" points="352,475 717,475 717,765 352,765 207,622"/>
    </svg>

    <div class="mark">
      <span class="mark__dot"></span>
      <span class="mark__name">inclusion<br>pledge</span>
    </div>

    <h1 class="headline">
      <div class="headline__lead">WE ARE ON THE</div>
      <div class="headline__key">LOOKOUT</div>
      <div class="headline__tail">FOR A</div>
    </h1>

    <ul class="roles">
      <li class="roles__item">OPERATIONS<br>AND HR MANAGER</li>
      <li class="roles__item">MEMBERSHIP ADVISOR<br>(EAST MIDLANDS)</li>
      <li class="roles__item">SOCIAL MEDIA<br>CONTENT CREATOR</li>
    </ul>

    <p class="tagline"><strong>THE UK’s FASTEST</strong><br>GROWING NETWORK FOR<br>MANUFACTURERS</p>

    <p class="footer">OFFICES IN<br>BIRMINGHAM AND LEEDS<br><span class="footer__note">WE ARE AN INCLUSIVE EMPLOYER</span></p>
  </article>
</main>
</body>
</html>
```